ZOR Clinic

We are a telemedicine based HIV treatment, prevention and hep c clinic looking to help make our online presence known.

Target Market(s)

Future patients. We want to this be informative and have stock images of all different types of people

Industry/Entity Type

Medical

Coding

Coded - Design and coding required

Requirements
Must have
• A Home Page, A page on PrEP, HIV treatment and Hep C. A box in the corner that says book now and a contact us page.

```html
<!DOCTYPE html>
<html lang="en">
<head>
<meta charset="utf-8">
<title>ZOR Clinic – Telemedicine HIV, PrEP & Hepatitis C Care</title>
<link href="https://fonts.googleapis.com/css2?family=Poppins:wght@400;500;600;700;800&display=swap" rel="stylesheet">
<style>
:root{
  --blue:#0c4ea3;
  --blue-deep:#083a86;
  --green:#6cc00c;
  --green-light:#8fd41c;
  --ink:#1d1d1f;
  --text:#444;
  --muted:#666;
  --soft:#eef3fa;
  --card:#ffffff;
  --dark:#2b2824;
}
*{margin:0;padding:0;box-sizing:border-box}
html,body{width:1200px;height:4781px;overflow:hidden}
body{font-family:"Poppins",sans-serif;color:var(--text);background:#fff;position:relative}
.abs{position:absolute}
.page{position:relative;width:1200px;height:4781px;overflow:hidden}
h1,h2,h3{font-family:"Poppins",sans-serif;color:var(--blue);font-weight:700}
.accent{color:var(--green)}
.btn{display:inline-block;border-radius:20px;font-weight:600;font-size:9.5px;text-decoration:none;padding:7px 18px}
.btn-green{background:var(--green);color:#fff}
.btn-outline{border:1.5px solid var(--green);color:#fff}

/* Hero */
.hero{left:0;top:0;width:1200px;height:724px;background:linear-gradient(100deg,#1f1c19 0%,#3b352f 45%,#6c655c 75%,#4a443d 100%)}
.hero-photo{left:560px;top:60px;width:640px;height:600px;background:radial-gradient(ellipse at 50% 45%,#9a9288 0%,#6d665d 45%,rgba(60,55,50,0) 75%)}
.brand{left:130px;top:26px;display:flex;align-items:center;gap:8px;color:#fff;font-weight:700;font-size:15px}
.brand-dot{width:16px;height:16px;border-radius:50%;background:var(--green)}
.nav-link{top:32px;font-size:9.5px;color:#fff;white-space:nowrap}
.nav-book{left:981px;top:25px;width:88px;height:26px;border-radius:14px;background:var(--green);color:#fff;font-size:9.5px;font-weight:600;display:flex;align-items:center;justify-content:center}
.hero-title{left:130px;top:226px;font-size:31px;line-height:35px;color:#fff;font-weight:700}
.hero-text{left:130px;top:348px;width:300px;font-size:10px;line-height:16px;color:#eee}
.hero-btns{left:130px;top:436px;display:flex;gap:8px}

/* Intro */
.intro-photo{left:154px;top:781px;width:414px;height:560px;border-radius:14px;background:linear-gradient(135deg,#c9d3d8 0%,#e7e1d8 40%,#b89c84 70%,#8b8f98 100%)}
.intro-title{left:649px;top:842px;font-size:25px;line-height:29px}
.intro-text{left:649px;top:910px;width:352px;font-size:10px;line-height:16px;color:var(--text)}
.feature{width:171px;height:190px;background:var(--card);border-radius:12px;box-shadow:0 6px 24px rgba(0,0,0,.09);text-align:center;top:1096px}
.feature svg{margin-top:36px}
.feature p{font-size:11px;font-weight:600;color:var(--ink);line-height:14px;margin-top:12px}

/* Services band */
.band{left:0;top:1440px;width:1200px;height:760px}
.section-title{width:1200px;left:0;text-align:center;font-size:25px}
.service{width:302px;height:397px;top:1625px;background:#fff;border-radius:14px;box-shadow:0 6px 22px rgba(12,78,163,.08)}
.service .ph{position:absolute;left:8px;top:6px;right:8px;height:196px;border-radius:10px}
.service h3{position:absolute;left:30px;top:234px;font-size:12px;color:var(--ink);font-weight:600}
.service p{position:absolute;left:30px;top:258px;width:245px;font-size:9.5px;line-height:15px;color:var(--text)}
.service .btn{position:absolute;left:30px;top:345px;padding:5px 16px;font-size:9px}

/* Steps */
.step{width:240px;text-align:center;top:2336px}
.step-icon{position:relative;width:104px;height:104px;margin:8px auto 0;border-radius:50%;background:var(--soft);display:flex;align-items:center;justify-content:center}
.step-num{position:absolute;left:0;bottom:2px;width:26px;height:26px;border-radius:50%;background:#fff;border:1px solid #ccc;font-size:10px;font-weight:700;color:var(--ink);display:flex;align-items:center;justify-content:center}
.step h3{font-size:12px;color:var(--ink);font-weight:600;margin-top:14px}
.step p{font-size:9.5px;line-height:15px;color:var(--text);margin-top:8px}

/* Values */
.values-sub{left:0;width:1200px;text-align:center;top:2658px;font-size:9.5px;line-height:15px;color:var(--text)}
.value{width:220px;text-align:center;top:2724px}
.value h3{font-size:12px;color:var(--ink);font-weight:600;margin-top:14px}
.value p{font-size:9.5px;line-height:15px;color:var(--text);margin-top:6px}

/* Mission */
.mission-title{color:#fff}
.mission-text{left:0;width:1200px;text-align:center;font-size:9.5px;line-height:15px;color:#e4ecf8}

/* FAQ */
.faq-photo{left:130px;top:3697px;width:417px;height:417px;border-radius:50%;background:radial-gradient(circle at 45% 40%,#f2f2f0 0%,#c8c8c6 45%,#5e5a55 85%)}
.faq-title{left:616px;top:3690px;font-size:25px}
.faq-item{left:614px;width:447px;background:#f0f0f0;border-radius:18px;font-size:11px;font-weight:600;color:var(--ink);padding:0 28px}
.faq-item .plus{position:absolute;right:20px;color:var(--green);font-size:16px;font-weight:600}
.faq-item p{font-weight:400;font-size:9.5px;line-height:15px;color:var(--text);margin-top:8px;width:300px}

/* CTA */
.cta{left:132px;top:4192px;width:936px;height:256px;border-radius:14px;background:linear-gradient(90deg,#3fa414 0%,#6cc00c 55%,#8bd21e 100%)}
.cta-photo{left:808px;top:4060px;width:240px;height:388px;border-radius:120px 120px 0 0;background:linear-gradient(180deg,#e8ecef 0%,#9fb4c4 55%,#2f7f87 100%)}
.cta h2{position:absolute;left:52px;top:92px;color:#fff;font-size:25px}
.cta p{position:absolute;left:50px;top:138px;width:430px;font-size:9.5px;line-height:15px;color:#f1ffe4}

/* Footer */
.foot-brand{left:130px;top:4540px;display:flex;align-items:center;gap:12px;color:var(--blue);font-weight:700;font-size:34px}
.foot-brand i{width:34px;height:34px;border-radius:50%;background:var(--green);display:block}
.foot-desc{left:130px;top:4652px;width:350px;font-size:9.5px;line-height:15px;color:var(--text)}
.foot-col{top:4556px;font-size:9.5px;line-height:15px;color:var(--text)}
.foot-col h4{color:var(--blue);font-size:11px;font-weight:600;margin-bottom:8px}
.foot-col li{list-style:none;display:flex;align-items:center;gap:5px}
.foot-bottom{left:130px;top:4738px;width:938px;display:flex;justify-content:space-between;font-size:9px;color:var(--text)}
</style>
</head>
<body>
<div class="page">

  <!-- Hero -->
  <section class="hero abs">
    <div class="hero-photo abs" role="img" aria-label="Man relaxing on a couch during a video call with a doctor on his laptop"></div>
    <svg class="abs" style="left:0;top:560px" width="1200" height="164" viewBox="0 0 1200 164" preserveAspectRatio="none">
      <path d="M0 90 C260 170 520 180 760 130 C960 90 1100 40 1200 60 L1200 164 L0 164 Z" fill="#0c4ea3"/>
      <path d="M0 100 C260 180 520 185 760 140 C960 100 1100 60 1200 78 L1200 164 L0 164 Z" fill="#1f73d2"/>
      <path d="M0 110 C260 190 520 190 760 150 C960 114 1100 78 1200 96 L1200 164 L0 164 Z" fill="#fff"/>
    </svg>
    <div class="brand abs"><span class="brand-dot"></span>ZOR Clinic</div>
    <span class="nav-link abs" style="left:501px">Home</span>
    <span class="nav-link abs" style="left:565px">PrEP</span>
    <span class="nav-link abs" style="left:620px">HIV Treatment</span>
    <span class="nav-link abs" style="left:724px">Hep C Treatment</span>
    <span class="nav-link abs" style="left:842px">About Us</span>
    <span class="nav-link abs" style="left:921px">Contact</span>
    <div class="nav-book abs">Book Now</div>
    <h1 class="hero-title abs">Expert HIV, PrEP<br><span class="accent">&amp; Hepatitis C Care</span><br>From Anywhere</h1>
    <p class="hero-text abs">Get confidential, compassionate healthcare through secure telemedicine appointments. Our experienced medical team provides personalized HIV prevention, HIV treatment, and Hepatitis C care designed around your needs.</p>
    <div class="hero-btns abs">
      <a class="btn btn-green">Book Your Appointment</a>
      <a class="btn btn-outline">Learn About Our Services</a>
    </div>
  </section>

  <!-- Intro -->
  <div class="intro-photo abs" role="img" aria-label="Smiling doctor in a white coat with a patient in a clinic"></div>
  <h2 class="intro-title abs">Healthcare That Meets<br><span class="accent">You Where You Are</span></h2>
  <div class="intro-text abs">
    <p>Access high-quality HIV prevention, treatment, and Hepatitis C care without the need for frequent clinic visits. Our telemedicine services make it easier to connect with healthcare providers from the comfort and privacy of your own space.</p>
    <p style="margin-top:16px">We believe everyone deserves respectful, judgment-free care with complete confidentiality.</p>
  </div>
  <div class="feature abs" style="left:352px">
    <svg width="60" height="60" viewBox="0 0 60 60" fill="none" stroke="#222" stroke-width="2"><path d="M30 6 L50 14 V30 C50 42 40 50 30 54 C20 50 10 42 10 30 V14 Z"/><rect x="22" y="28" width="16" height="12" rx="2"/><path d="M25 28 V23 a5 5 0 0 1 10 0 V28"/></svg>
    <p>Private &amp; Secure<br>Telemedicine Visits</p>
  </div>
  <div class="feature abs" style="left:534px">
    <svg width="60" height="60" viewBox="0 0 60 60" fill="none" stroke="#222" stroke-width="2"><rect x="10" y="10" width="40" height="40" rx="6"/><path d="M30 20 V40 M20 30 H40"/></svg>
    <p>Experienced<br>Healthcare Providers</p>
  </div>
  <div class="feature abs" style="left:716px">
    <svg width="60" height="60" viewBox="0 0 60 60" fill="none" stroke="#222" stroke-width="2"><rect x="8" y="12" width="44" height="30" rx="3"/><path d="M22 50 H38 M30 42 V50"/><circle cx="44" cy="12" r="6" fill="#fff"/></svg>
    <p>Convenient<br>Online Appointments</p>
  </div>
  <div class="feature abs" style="left:898px">
    <svg width="60" height="60" viewBox="0 0 60 60" fill="none" stroke="#222" stroke-width="2"><rect x="12" y="8" width="32" height="44" rx="3"/><path d="M18 20 l3 3 5-5 M30 21 H38 M18 32 l3 3 5-5 M30 33 H38 M18 44 H34"/></svg>
    <p>Personalized<br>Treatment Plans</p>
  </div>

  <!-- Services band -->
  <svg class="band abs" viewBox="0 0 1200 760" preserveAspectRatio="none">
    <path d="M0 70 C260 10 520 10 760 40 C960 64 1100 30 1200 0 L1200 700 C1000 620 820 640 620 700 C420 760 200 730 0 660 Z" fill="#eef3fa"/>
  </svg>
  <h2 class="section-title abs" style="top:1564px">Comprehensive Care <span class="accent">For Your Health</span></h2>
  <div class="service abs" style="left:130px">
    <div class="ph" role="img" aria-label="Open pill bottle with blue tablets spilled on a white surface" style="background:linear-gradient(135deg,#f3f3f3,#dcdcdc 60%,#2f6fc4)"></div>
    <h3>PrEP (HIV Prevention)</h3>
    <p>Protect yourself from HIV with proven prevention options. Our providers help you understand whether PrEP is right for you and guide you through the entire process.</p>
    <a class="btn btn-green">Learn More</a>
  </div>
  <div class="service abs" style="left:449px">
    <div class="ph" role="img" aria-label="Hands passing a prescription bottle across a desk" style="background:linear-gradient(135deg,#4a2f22,#8b5e44 50%,#d9cfc4)"></div>
    <h3>HIV Treatment</h3>
    <p>Living with HIV? Our team provides ongoing medical support, treatment guidance, and personalized care plans to help you maintain your health.</p>
    <a class="btn btn-green">Learn More</a>
  </div>
  <div class="service abs" style="left:764px">
    <div class="ph" role="img" aria-label="Caregiver helping an older woman with her medication at home" style="background:linear-gradient(135deg,#7a5a48,#c09a7c 50%,#2c3552)"></div>
    <h3>Hepatitis C Treatment</h3>
    <p>Effective treatment options are available for Hepatitis C. Our specialists provide evaluation, support, and care throughout your treatment journey.</p>
    <a class="btn btn-green">Learn More</a>
  </div>

  <!-- Steps -->
  <h2 class="section-title abs" style="top:2283px">Getting Care <span class="accent">Is Simple</span></h2>
  <div class="step abs" style="left:205px">
    <div class="step-icon">
      <svg width="40" height="40" viewBox="0 0 40 40" fill="none" stroke="#222" stroke-width="2"><rect x="4" y="8" width="32" height="28" rx="3"/><path d="M4 16 H36 M12 4 V12 M28 4 V12"/></svg>
      <span class="step-num">01</span>
    </div>
    <h3>Book Your Appointment</h3>
    <p>Schedule a confidential online consultation<br>with our healthcare team.</p>
  </div>
  <div class="step abs" style="left:479px">
    <div class="step-icon">
      <svg width="40" height="40" viewBox="0 0 40 40" fill="none" stroke="#222" stroke-width="2"><path d="M8 30 H32 a7 7 0 0 0 -2 -14 a11 11 0 0 0 -21 3 a6 6 0 0 0 -1 11 Z"/></svg>
      <span class="step-num">02</span>
    </div>
    <h3>Meet Your Provider Online</h3>
    <p>Discuss your health concerns through a<br>secure telemedicine visit.</p>
  </div>
  <div class="step abs" style="left:757px">
    <div class="step-icon">
      <svg width="40" height="40" viewBox="0 0 40 40" fill="none" stroke="#222" stroke-width="2"><circle cx="20" cy="16" r="10"/><path d="M15 16 l4 4 7-7"/></svg>
      <span class="step-num">03</span>
    </div>
    <h3>Receive Personalized Care</h3>
    <p>Get treatment recommendations, prescriptions, and ongoing support.</p>
  </div>

  <!-- Values -->
  <h2 class="section-title abs" style="top:2612px">Healthcare Built <span class="accent">Around You</span></h2>
  <p class="values-sub abs">We combine medical expertise with convenient telemedicine technology to make HIV<br>prevention and treatment easier, accessible, and stress-free.</p>
  <div class="value abs" style="left:144px">
    <svg width="56" height="56" viewBox="0 0 56 56" fill="none" stroke="#222" stroke-width="2"><path d="M14 6 H34 L44 16 V50 H14 Z"/><rect x="22" y="30" width="14" height="12" rx="2"/><path d="M25 30 V26 a4 4 0 0 1 8 0 V30"/></svg>
    <h3>Confidential Care</h3>
    <p>Your privacy and comfort are always<br>our priority.</p>
  </div>
  <div class="value abs" style="left:376px">
    <svg width="56" height="56" viewBox="0 0 56 56" fill="none" stroke="#222" stroke-width="2"><rect x="10" y="10" width="36" height="36" rx="6"/><path d="M28 18 V38 M18 28 H38"/></svg>
    <h3>Expert Medical Support</h3>
    <p>Receive care from experienced<br>healthcare professionals.</p>
  </div>
  <div class="value abs" style="left:613px">
    <svg width="56" height="56" viewBox="0 0 56 56" fill="none" stroke="#222" stroke-width="2"><circle cx="30" cy="22" r="12"/><path d="M24 22 l4 4 8-8"/><path d="M8 44 C18 36 28 40 38 42 L50 36"/></svg>
    <h3>Convenient Telemedicine</h3>
    <p>Access treatment without unnecessary travel.</p>
  </div>
  <div class="value abs" style="left:847px">
    <svg width="56" height="56" viewBox="0 0 56 56" fill="none" stroke="#222" stroke-width="2"><rect x="12" y="8" width="32" height="42" rx="3"/><rect x="20" y="26" width="22" height="22" rx="2" fill="#fff"/><path d="M31 31 V43 M25 37 H37"/><path d="M18 16 H36"/></svg>
    <h3>Patient-Centered Approach</h3>
    <p>Every care plan is tailored to your individual needs.</p>
  </div>
  <svg class="abs" style="left:0;top:2860px" width="1200" height="340" viewBox="0 0 1200 340" fill="none">
    <g stroke="#cfe6a8" stroke-width="1.5">
      <path d="M252 14 V80 Q252 92 264 92 H412"/>
      <path d="M486 14 V80 Q486 92 498 92 H580"/>
      <path d="M723 14 V80 Q723 92 711 92 H620"/>
      <path d="M957 14 V80 Q957 92 945 92 H790"/>
      <path d="M600 92 V130"/>
    </g>
    <g fill="#0c4ea3"><circle cx="252" cy="13" r="5"/><circle cx="486" cy="13" r="5"/><circle cx="723" cy="13" r="5"/><circle cx="957" cy="13" r="5"/></g>
    <circle cx="600" cy="230" r="94" fill="#eef3fa" stroke="#d7e4f4" stroke-width="2"/>
  </svg>

  <!-- Mission -->
  <svg class="abs" style="left:0;top:3209px" width="1200" height="390" viewBox="0 0 1200 390" preserveAspectRatio="none">
    <defs><linearGradient id="missionGrad" x1="0" y1="0" x2="1" y2="1"><stop offset="0" stop-color="#0a4596"/><stop offset="1" stop-color="#0c63c4"/></linearGradient></defs>
    <path d="M0 70 C240 20 420 60 620 80 C860 104 1040 30 1200 0 L1200 340 C1020 380 860 370 640 330 C420 290 200 300 0 360 Z" fill="url(#missionGrad)"/>
  </svg>
  <h2 class="section-title mission-title abs" style="top:3316px">Compassionate Care <span class="accent">Without Judgment</span></h2>
  <div class="mission-text abs" style="top:3362px">
    <p>Our mission is to provide accessible, reliable, and confidential healthcare for individuals seeking HIV<br>prevention, HIV treatment, and Hepatitis C services.</p>
    <p style="margin-top:14px">Through telemedicine, we remove barriers to care and help patients receive the support they need<br>wherever they are.</p>
  </div>

  <!-- FAQ -->
  <div class="faq-photo abs" role="img" aria-label="Tablet on a desk showing a video consultation with a doctor"></div>
  <h2 class="faq-title abs">Frequently Asked <span class="accent">Questions</span></h2>
  <div class="faq-item abs" style="top:3740px;height:57px;line-height:57px">What is telemedicine HIV care?<span class="plus" style="top:0">+</span></div>
  <div class="faq-item abs" style="top:3805px;height:57px;line-height:57px">Is my information private?<span class="plus" style="top:0">+</span></div>
  <div class="faq-item abs" style="top:3871px;height:58px;line-height:58px">How do I start treatment?<span class="plus" style="top:0">+</span></div>
  <div class="faq-item abs" style="top:3936px;height:101px;padding-top:20px">Can I get PrEP through telemedicine?<span class="plus" style="top:14px">−</span>
    <p>Yes, our providers can evaluate your needs and discuss PrEP options with you.</p>
  </div>

  <!-- CTA -->
  <div class="cta abs">
    <h2>Ready To Take Control Of Your Health?</h2>
    <p>Getting expert HIV prevention, treatment, and Hepatitis C care is easier than ever. Schedule your confidential online appointment today.</p>
  </div>
  <div class="cta-photo abs" role="img" aria-label="Doctor in scrubs and glasses seated, writing on a clipboard"></div>

  <!-- Footer -->
  <div class="foot-brand abs"><i></i>ZOR Clinic</div>
  <p class="foot-desc abs">Providing confidential telemedicine healthcare for HIV prevention,<br>HIV treatment, and Hepatitis C care.</p>
  <div class="foot-col abs" style="left:621px">
    <h4>Services</h4>
    <ul><li>PrEP</li><li>HIV Treatment</li><li>Hep C Treatment</li><li>Telemedicine Visits</li></ul>
  </div>
  <div class="foot-col abs" style="left:779px">
    <h4>Quick Links</h4>
    <ul><li>About Us</li><li>Contact</li><li>Privacy Policy</li><li>Terms &amp; Conditions</li></ul>
  </div>
  <div class="foot-col abs" style="left:933px">
    <h4>Contact</h4>
    <ul>
      <li><svg width="9" height="9" viewBox="0 0 10 10"><path d="M2 0 L4 2 L3 4 Q4 6 6 7 L8 6 L10 8 L8 10 Q2 9 0 2 Z" fill="#6cc00c"/></svg>Phone: XXX-XXX-XXXX</li>
      <li><svg width="9" height="9" viewBox="0 0 10 10"><rect x="0" y="2" width="10" height="7" rx="1" fill="#6cc00c"/></svg>Email: info@zorclinic.example</li>
    </ul>
  </div>
  <div class="foot-bottom abs">
    <span>© 2026 ZOR Clinic. All Rights Reserved.</span>
    <span>Confidential Healthcare | Secure Telemedicine Services</span>
  </div>

</div>
</body>
</html>
```